American pesto sauce company needs a vintage/ old fashioned package design

Company name: Marisol Grove.
We need a food label design for 4 different flavors of pesto sauce: classic almond, sundried tomato, roasted red pepper, and Cajun spice. For those that do not know what pesto is, it is a sauce like tomato sauce that is traditionally Italian and goes on pasta or whatever you choose to put it on and the consistent ingredients are garlic, cheese, nuts, olive oil and basil. They are fresh, all natural without preservatives, artificial flavors or colors.
The design of the jar is an old fashioned wire bale jar used for preserving foods ( attached is a picture). I'm looking for a label with:
• an upscale vintage feel but will also stand out on a grocery store shelf. I have attached an example of the feel I am looking for as well as the format of the words with my company name.
• The word "Pesto" must be prominent on the label.
• metalic gold boarders that go around the whole label maybe with gold embellishments if you see fit for that upscale feeling.
• Also, as you can see in the attachment, there are different typesets. And it must be easy to read from at least 3 feet away.
• Each label will have a different color corresponding to the flavor- could be part of the flavor text
• The bottom of the front panel must have “Net Wt. 5.75 oz (162g)” in a creative format how you see fit. Measures: height-28 mm, width-75mm
• Need logo for top part of label with the letters MG for Marisol Grove and it will also contain the website, address and parent company name, use by date, etc. Measures:50 mm diameter
• The back panel of the label will contain the nutrition facts, ingredients and bar code. Measures: height-28 mm, width-75mm

Also the label is one piece with 3 different sections. Attached will be an example with measurements.
Updates

Check out this website on packaging. I absolutely love love love the Hartwell Pantry almond water labels. The colors for the different flavors. How its not just horizontal or vertical. The different typesets/fonts/typography. The flourishes and background thats faded.
http://brightwrapgallery.com/page/3/

Target Market(s)

Target market is medium- high income foodies between 35-65

Industry/Entity Type

Grocery Store

Requirements
Must have
• Net Wt on front lower panel. Separation of the company name Marisol & Pesto. See attachment.
Nice to have
• Name of flavor designed in a wave pattern as shown in attachment. Hand drawn font OK.

```html
<!DOCTYPE html>
<html lang="en">
<head>
<meta charset="utf-8">
<title>Marisol Grove Pesto Labels</title>
<link href="https://fonts.googleapis.com/css2?family=Playfair+Display+SC:wght@700&family=Yesteryear&family=Archivo:wght@400;600&display=swap" rel="stylesheet">
<style>
  :root {
    --backdrop: #e8e1d6;
    --label-cream: #f4ede1;
    --label-edge: #b58a4a;
    --ink-maroon: #5e1a1b;
    --ink-brown: #4a241c;
    --flavor-almond: #4a1c17;
    --flavor-tomato: #a8202b;
    --almond-tone: #a8703f;
    --tomato-tone: #9c2a20;
  }
  html, body {
    margin: 0;
    width: 1200px;
    height: 1200px;
    overflow: hidden;
    background: var(--backdrop);
  }
  .label-sheet { display: block; width: 1200px; height: 1200px; }
  .label-outline { fill: none; stroke: var(--label-edge); stroke-width: 6; }
  .label-body { fill: var(--label-cream); }
  .panel-dots { fill: none; stroke: var(--ink-maroon); stroke-width: 1.6; stroke-dasharray: 1.5 4; stroke-linecap: round; }
  .seal-rule { fill: none; stroke: var(--label-edge); stroke-width: 1.5; }
  .seal-dot { fill: var(--ink-maroon); }
  .brand-name { font-family: "Playfair Display SC", serif; font-weight: 700; font-size: 22px; fill: var(--ink-maroon); text-anchor: middle; }
  .seal-ring-text { font-family: "Archivo", sans-serif; font-size: 11px; letter-spacing: 3px; fill: var(--ink-brown); }
  .strip-rule { stroke: var(--ink-maroon); stroke-width: 1.4; }
  .est-mark { font-family: "Playfair Display SC", serif; font-size: 12px; fill: var(--ink-maroon); }
  .pesto-word { font-family: "Playfair Display SC", serif; font-weight: 700; font-size: 34px; letter-spacing: 2px; fill: var(--ink-maroon); text-anchor: middle; }
  .flavor-name { font-family: "Yesteryear", cursive; font-size: 54px; text-anchor: middle; }
  .flavor-almond { fill: var(--flavor-almond); }
  .flavor-tomato { fill: var(--flavor-tomato); }
  .tagline { font-family: "Archivo", sans-serif; font-weight: 600; font-size: 11px; letter-spacing: 1.5px; fill: var(--ink-brown); }
  .weight { font-family: "Archivo", sans-serif; font-size: 12px; fill: var(--ink-brown); }
  .tag-rule { stroke: var(--ink-maroon); stroke-width: 1.2; }
</style>
</head>
<body>
<svg class="label-sheet" viewBox="0 0 1200 1200" xmlns="http://www.w3.org/2000/svg">
  <defs>
    <path id="panel-shape" d="M22,0 H438 A22,22 0 0 0 460,22 V168 A22,22 0 0 0 438,190 H22 A22,22 0 0 0 0,168 V22 A22,22 0 0 0 22,0 Z"/>
    <path id="panel-inner" d="M20,0 H400 A20,20 0 0 0 420,20 V130 A20,20 0 0 0 400,150 H20 A20,20 0 0 0 0,130 V20 A20,20 0 0 0 20,0 Z"/>
    <path id="seal-ring-path" d="M0,140 m-104,0 a104,104 0 1,1 208,0 a104,104 0 1,1 -208,0"/>
    <g id="label-shell">
      <circle class="label-outline" cx="0" cy="140" r="130"/>
      <rect class="label-outline" x="-48" y="200" width="96" height="340"/>
      <use href="#panel-shape" class="label-outline" x="-230" y="520"/>
      <circle class="label-body" cx="0" cy="140" r="130"/>
      <rect class="label-body" x="-48" y="200" width="96" height="340"/>
      <use href="#panel-shape" class="label-body" x="-230" y="520"/>
      <circle class="seal-rule" cx="0" cy="140" r="118"/>
      <circle class="seal-rule" cx="0" cy="140" r="90"/>
      <circle class="seal-dot" cx="0" cy="108" r="24"/>
      <text class="brand-name" x="0" y="162">Marisol Grove</text>
      <text class="seal-ring-text"><textPath href="#seal-ring-path">FRESH · ALL NATURAL · NO PRESERVATIVES</textPath></text>
      <line class="strip-rule" x1="0" y1="300" x2="0" y2="470"/>
      <use href="#panel-inner" class="panel-dots" x="-210" y="540"/>
      <text class="est-mark" x="-92" y="582">est</text>
      <text class="pesto-word" x="0" y="584">PESTO</text>
      <text class="tagline" x="-150" y="664">MOST</text>
      <line class="tag-rule" x1="-150" y1="650" x2="-60" y2="650"/>
      <line class="tag-rule" x1="60" y1="650" x2="150" y2="650"/>
      <text class="tagline" x="150" y="664" text-anchor="end">DELICIOUS</text>
      <text class="weight" x="-110" y="686">162g</text>
      <text class="weight" x="150" y="686" text-anchor="end">Net Wt. 5.75 oz</text>
    </g>
  </defs>

  <g class="label label-almond" transform="translate(320 230)">
    <use href="#label-shell"/>
    <text class="flavor-name flavor-almond" x="0" y="638">Classic Almond</text>
    <ellipse cx="0" cy="684" rx="34" ry="18" fill="var(--almond-tone)" role="img" aria-label="Illustration of two almonds"/>
  </g>

  <g class="label label-tomato" transform="translate(880 230)">
    <use href="#label-shell"/>
    <text class="flavor-name flavor-tomato" x="0" y="638">Sun Dried Tomato</text>
    <ellipse cx="0" cy="684" rx="34" ry="18" fill="var(--tomato-tone)" role="img" aria-label="Illustration of sun dried tomatoes"/>
  </g>
</svg>
</body>
</html>
```